Canadian furniture distributor

I need a logo design for my new company, Pellham Craft G.P., Ergonomic High-End furniture distribution (very attractive patented design -mainly Desks & Chairs-).

Can be used for children adults, elders or limited mobility people.

Colors and design should match logo colors and products.

Industry/Entity Type

It Company

```html
<!DOCTYPE html>
<html lang="en">
<head>
<meta charset="utf-8">
<title>Pellham Craft – Business Card</title>
<link rel="stylesheet" href="https://fonts.googleapis.com/css2?family=Montserrat:wght@500;600;700&display=swap">
<style>
  :root {
    --backdrop: #251017;
    --card: #ffffff;
    --plum: #8c1f50;
    --gold: #f5b316;
    --photo-light: #f1f2f4;
    --photo-dark: #c9ccd2;
  }
  html, body {
    margin: 0;
    padding: 0;
    width: 1200px;
    height: 1000px;
    overflow: hidden;
    background: var(--backdrop);
    font-family: "Montserrat", Arial, sans-serif;
  }
  .canvas {
    position: relative;
    width: 1200px;
    height: 1000px;
    background: var(--backdrop);
  }
  .card {
    position: absolute;
    left: 276px;
    width: 649px;
    height: 379px;
    background: var(--card);
    overflow: hidden;
    box-shadow: 4px 5px 8px rgba(0, 0, 0, 0.55);
  }
  .card--front { top: 115px; }
  .card--back { top: 532px; }
  .card__art {
    position: absolute;
    inset: 0;
    width: 649px;
    height: 379px;
  }
  .brand-name {
    position: absolute;
    margin: 0;
    color: var(--plum);
    font-weight: 700;
    letter-spacing: -0.5px;
    white-space: nowrap;
  }
  .card--front .brand-name {
    left: 38px;
    top: 124px;
    font-size: 38px;
  }
  .card--back .brand-name {
    left: 0;
    right: 0;
    top: 215px;
    text-align: center;
    font-size: 42px;
  }
  .person-name {
    position: absolute;
    left: 38px;
    top: 183px;
    margin: 0;
    font-size: 25px;
    font-weight: 500;
    color: var(--plum);
  }
  .person-title {
    position: absolute;
    left: 41px;
    top: 214px;
    margin: 0;
    font-size: 18px;
    font-weight: 500;
    color: var(--gold);
  }
  .product-photo {
    position: absolute;
    left: 419px;
    top: 50px;
    width: 186px;
    height: 155px;
    border-radius: 6px;
    background: linear-gradient(160deg, var(--photo-light), var(--photo-dark));
  }
  .contact-list {
    position: absolute;
    left: 42px;
    top: 284px;
    margin: 0;
    padding: 0;
    list-style: none;
  }
  .contact-list li {
    display: flex;
    align-items: center;
    height: 21.5px;
    font-size: 16px;
    font-weight: 500;
    color: var(--plum);
  }
  .contact-icon {
    width: 18px;
    height: 18px;
    margin-right: 9px;
    flex: none;
  }
</style>
</head>
<body>
<main class="canvas">

  <section class="card card--front" aria-label="Business card front">
    <svg class="card__art" viewBox="0 0 649 379" aria-hidden="true">
      <circle cx="649" cy="22" r="304" fill="none" stroke="var(--plum)" stroke-width="14"/>
      <circle cx="649" cy="22" r="287" fill="none" stroke="var(--gold)" stroke-width="5"/>
      <path d="M0,248 C250,238 470,288 546,379 L494,379 C420,305 230,262 0,254 Z" fill="var(--plum)"/>
      <path d="M0,257 C210,262 390,300 470,379 L414,379 C350,318 210,272 0,261 Z" fill="var(--gold)"/>
    </svg>

    <div class="product-photo" role="img" aria-label="Photo of a white height-adjustable ergonomic desk"></div>

    <h1 class="brand-name">Pellham Craft</h1>
    <p class="person-name">Your name</p>
    <p class="person-title">Title</p>

    <ul class="contact-list">
      <li>
        <svg class="contact-icon" viewBox="0 0 18 18" aria-hidden="true">
          <circle cx="9" cy="9" r="9" fill="var(--gold)"/>
          <path d="M9 4.2a3 3 0 0 0-3 3c0 2.2 3 6.3 3 6.3s3-4.1 3-6.3a3 3 0 0 0-3-3z" fill="#fff"/>
          <circle cx="9" cy="7.2" r="1.1" fill="var(--gold)"/>
        </svg>
        your address
      </li>
      <li>
        <svg class="contact-icon" viewBox="0 0 18 18" aria-hidden="true">
          <circle cx="9" cy="9" r="9" fill="var(--gold)"/>
          <path d="M5.2 5.6l1.7-1.1 1.4 2.3-1 .8c.5 1.2 1.3 2 2.4 2.6l.8-1 2.3 1.4-1.1 1.7c-3.2-.4-6.1-3.4-6.5-6.7z" fill="#fff"/>
        </svg>
        123 456 7890
      </li>
      <li>
        <svg class="contact-icon" viewBox="0 0 18 18" aria-hidden="true">
          <circle cx="9" cy="9" r="9" fill="var(--gold)"/>
          <rect x="4.5" y="5.8" width="9" height="6.4" rx="0.8" fill="#fff"/>
          <path d="M4.8 6.2L9 9.4l4.2-3.2" fill="none" stroke="var(--gold)" stroke-width="1"/>
        </svg>
        yourname@yourdomain.com
      </li>
    </ul>
  </section>

  <section class="card card--back" aria-label="Business card back">
    <svg class="card__art" viewBox="0 0 649 379" aria-hidden="true">
      <path d="M152,0 L222,0 C300,50 470,74 649,81 L649,86 C420,82 230,60 152,0 Z" fill="var(--plum)"/>
      <path d="M232,0 L290,0 C360,40 500,68 649,77 L649,80 C470,72 310,45 232,0 Z" fill="var(--gold)"/>
      <path d="M0,293 C240,286 420,320 494,379 L446,379 C380,330 220,302 0,299 Z" fill="var(--plum)"/>
      <path d="M0,301 C190,304 340,330 414,379 L366,379 C300,342 190,314 0,305 Z" fill="var(--gold)"/>
    </svg>
    <h2 class="brand-name">Pellham Craft</h2>
  </section>

</main>
</body>
</html>
```